Automotive eCommerce Business looking for a business card design

Looking for a clean and simple business card design. Our company name is "Harbor Crest Auto" and we are a company specializing in the ecommerce sales of automotive parts, specifically for pick up trucks and large SUVs. Our company colours are red, black, and white.

Feel free to use the logo provided or create a new logo that you seem fit. Looking forward to your creative ideas!

Industry/Entity Type

Automotive

Contact Information for Business Card

We were thinking of a possibly two-sided design featuring just the logo and company name on one side, and personal information on the other side. Single sided designs will be considered as well.

Font styles to use
Serif
Sans Serif
Decorative

Colors
ec1f27
ffffff
000000

Requirements
Must have
• Space for employee's name, title, phone number and email address, along with the company address and website somewhere.

```html
<!DOCTYPE html>
<html lang="en">
<head>
<meta charset="utf-8">
<title>Harbor Crest Auto – Business Card</title>
<link rel="stylesheet" href="https://fonts.googleapis.com/css2?family=Open+Sans:wght@400;600;700;800&display=swap">
<style>
  :root {
    --brand-red: #ec1f27;
    --card-black: #1e1c1d;
    --ink-white: #ffffff;
    --stage: #2c2e2d;
  }
  * { box-sizing: border-box; margin: 0; padding: 0; }
  html, body {
    width: 1200px; height: 1200px; overflow: hidden;
    background: var(--stage);
    font-family: "Open Sans", sans-serif;
  }
  .sheet {
    width: 1200px; height: 1200px;
    display: flex; flex-direction: column;
    align-items: center; justify-content: center; gap: 60px;
  }
  .card {
    width: 900px; height: 514px;
    background: var(--card-black);
    border-radius: 28px;
    position: relative;
    box-shadow: 0 18px 40px rgba(0,0,0,.45);
  }
  /* Back: brand side */
  .card--brand {
    display: flex; align-items: center; justify-content: center; gap: 22px;
  }
  .brand-mark {
    width: 34px; height: 34px; border-radius: 50%;
    background: var(--ink-white);
  }
  .brand-name {
    color: var(--ink-white);
    font-weight: 800; font-size: 46px; letter-spacing: 1px;
    text-transform: uppercase;
  }
  /* Front: contact side */
  .card--contact { display: flex; align-items: center; padding: 0 70px; }
  .contact-brand {
    width: 330px; display: flex; align-items: center; gap: 14px;
  }
  .contact-brand .mark {
    width: 26px; height: 26px; border-radius: 50%; background: var(--brand-red); flex: none;
  }
  .contact-brand .name {
    color: var(--brand-red); font-weight: 800; font-size: 30px; line-height: 1.15;
    text-transform: uppercase;
  }
  .contact-details { color: var(--ink-white); padding-left: 30px; }
  .person-name {
    color: var(--brand-red); font-weight: 700; font-size: 34px;
    text-transform: uppercase; letter-spacing: .5px;
  }
  .person-title { font-size: 22px; margin-bottom: 22px; }
  .detail-line { display: flex; align-items: center; gap: 12px; font-size: 22px; line-height: 1.55; }
  .detail-line svg { width: 18px; height: 18px; flex: none; fill: var(--brand-red); }
  .address { font-size: 22px; line-height: 1.5; margin-top: 4px; }
</style>
</head>
<body>
<main class="sheet">
  <section class="card card--brand" aria-label="Card back">
    <span class="brand-mark"></span>
    <span class="brand-name">Harbor Crest Auto Ltd.</span>
  </section>

  <section class="card card--contact" aria-label="Card front">
    <div class="contact-brand">
      <span class="mark"></span>
      <span class="name">Harbor Crest<br>Auto</span>
    </div>
    <div class="contact-details">
      <p class="person-name">Marcus Delaney</p>
      <p class="person-title">Managing Director</p>
      <p class="detail-line">
        <svg viewBox="0 0 24 24" aria-hidden="true"><path d="M6.6 10.8a15.1 15.1 0 0 0 6.6 6.6l2.2-2.2a1 1 0 0 1 1-.25 11.4 11.4 0 0 0 3.6.57 1 1 0 0 1 1 1V20a1 1 0 0 1-1 1A17 17 0 0 1 3 4a1 1 0 0 1 1-1h3.5a1 1 0 0 1 1 1c0 1.25.2 2.45.57 3.57a1 1 0 0 1-.25 1z"/></svg>
        555 014 2276
      </p>
      <p class="detail-line">
        <svg viewBox="0 0 24 24" aria-hidden="true"><path d="M2 21l21-9L2 3v7l15 2-15 2z"/></svg>
        marcus@harborcrestauto.com
      </p>
      <p class="detail-line">
        <svg viewBox="0 0 24 24" aria-hidden="true"><path d="M12 2a7 7 0 0 0-7 7c0 5.25 7 13 7 13s7-7.75 7-13a7 7 0 0 0-7-7zm0 9.5A2.5 2.5 0 1 1 12 6.5a2.5 2.5 0 0 1 0 5z"/></svg>
        www.harborcrestauto.com
      </p>
      <p class="address">1480 Larkspur Ave<br>Millbrook, LA 70912</p>
    </div>
  </section>
</main>
</body>
</html>
```